Begegnungskonzert Kammerchor Lumivessa Berlin und Tonbrückener Kinderchor Peking
Zielgruppe
Es geht um ein Konzertplakat für den Kammerchor Lumivessa Berlin. www.lumivessa-chor.example
Wir haben ein Begegnungskonzert mit einem Chinesischen Kinderchor, der Berlin besucht.
Aufgabenstellung
Kammerchor Lumivessa Berlin, Leitung: Karsten Brodt
Tonbrückener Kinderchor Peking, Leitung: Prof. Zhou Wen
21.08.2017, 19:00 Uhr Quellkapelle Berlin Wilmersdorf, Falkenauer Str. 27, 14183 Berlin
Eintritt frei, Spenden erbeten
Werke von Albrechtsen, Caspo, Thornvik, Pemberley und vielen mehr...
Logos und Farben bitte von unserer Website übernehmen!

```html
<!DOCTYPE html>
<html lang="de">
<head>
<meta charset="utf-8">
<title>Begegnungskonzert Berlin//Peking</title>
<link href="https://fonts.googleapis.com/css2?family=Roboto:wght@300;400;500;700&display=swap" rel="stylesheet">
<style>
  :root {
    --ink: #111111;
    --paper: #ffffff;
    --stage: #ececec;
    --muted: #555555;
    --photo-dark: #5a4a3c;
    --photo-warm: #a9794f;
    --photo-light: #f3e2d0;
    --veil: rgba(70, 70, 70, 0.55);
  }
  * { margin: 0; padding: 0; box-sizing: border-box; }
  html, body { width: 1200px; height: 928px; overflow: hidden; background: var(--stage); }
  body { font-family: "Roboto", sans-serif; color: var(--ink); }

  .poster-frame {
    position: absolute; left: 294px; top: 24px;
    width: 574px; height: 826px;
    transform: scale(1.065); transform-origin: 0 0;
  }
  .poster {
    position: relative; width: 574px; height: 826px;
    background: var(--paper); overflow: hidden;
    box-shadow: 0 2px 10px rgba(0,0,0,0.15);
  }
  .poster-shapes { position: absolute; inset: 0; }

  .brand {
    position: absolute; left: 34px; top: 78px;
    display: flex; align-items: center; gap: 6px;
    color: var(--paper); font-weight: 400; font-size: 14px; line-height: 1.05;
  }
  .brand-dot { width: 8px; height: 8px; border-radius: 50%; background: var(--paper); }

  .ensembles { position: absolute; right: 35px; top: 38px; text-align: right; }
  .ensemble { margin-bottom: 17px; }
  .ensemble-name { font-weight: 700; font-size: 14px; line-height: 16px; text-transform: uppercase; }
  .ensemble-lead { font-weight: 300; font-size: 11px; line-height: 15px; }

  .title {
    position: absolute; left: 35px; top: 398px;
    font-weight: 700; font-size: 40px; line-height: 44px;
    text-transform: uppercase; letter-spacing: 0.2px;
  }

  .event-info { position: absolute; left: 35px; top: 745px; }
  .event-date { font-weight: 500; font-size: 14px; line-height: 18px; }
  .event-venue { font-weight: 300; font-size: 11px; line-height: 16px; color: var(--muted); }

  .program { position: absolute; right: 35px; top: 739px; text-align: right; }
  .program-intro { font-weight: 300; font-size: 11px; line-height: 16px; color: var(--muted); }
  .program-works { font-weight: 700; font-size: 14px; line-height: 21px; text-transform: uppercase; }
</style>
</head>
<body>
  <div class="poster-frame">
    <article class="poster">
      <svg class="poster-shapes" viewBox="0 0 574 826" width="574" height="826">
        <defs>
          <linearGradient id="choirChurch" x1="0" y1="0" x2="1" y2="1">
            <stop offset="0" stop-color="#8a8c90"/>
            <stop offset="0.5" stop-color="#5a4a3c"/>
            <stop offset="1" stop-color="#3a2e26"/>
          </linearGradient>
          <linearGradient id="choirHall" x1="0" y1="0" x2="0" y2="1">
            <stop offset="0" stop-color="#7a5436"/>
            <stop offset="0.35" stop-color="#c08f63"/>
            <stop offset="0.7" stop-color="#efd4b8"/>
            <stop offset="1" stop-color="#f8ebdf"/>
          </linearGradient>
        </defs>
        <polygon points="0,22 242,94 0,164" fill="var(--ink)"/>
        <polygon role="img" aria-label="Foto: Kammerchor mit Dirigent und Bläsern in einer Kirche"
                 points="0,164 242,94 574,180 574,455 95,330 0,345" fill="url(#choirChurch)"/>
        <polygon role="img" aria-label="Foto: Chor im Halbkreis mit Dirigent in einem Konzertsaal"
                 points="0,625 574,545 574,826 0,826" fill="url(#choirHall)"/>
        <polygon points="370,560 574,445 574,548" fill="var(--veil)"/>
      </svg>

      <div class="brand"><span class="brand-dot"></span><span>Lumivessa<br>Berlin</span></div>

      <div class="ensembles">
        <div class="ensemble">
          <p class="ensemble-name">Kammerchor Lumivessa<br>Berlin</p>
          <p class="ensemble-lead">Leitung: Karsten Brodt</p>
        </div>
        <div class="ensemble">
          <p class="ensemble-name">Tonbrückener Kinderchor<br>Peking</p>
          <p class="ensemble-lead">Leitung: Prof. Zhou Wen</p>
        </div>
      </div>

      <h1 class="title">Begegnungs<br>Konzert<br>Berlin//Peking</h1>

      <div class="event-info">
        <p class="event-date">21. AUGUST 2017 // 19 UHR</p>
        <p class="event-venue">Quellkapelle Berlin Wilmersdorf</p>
        <p class="event-venue">Falkenauer Str. 27 // 14183 Berlin</p>
      </div>

      <div class="program">
        <p class="program-intro">Werke von</p>
        <p class="program-works">Albrechtsen, Caspo, Thornvik,<br>Pemberley und vielen mehr</p>
      </div>
    </article>
  </div>
</body>
</html>
```